Stylist/Barber Standup Sign for Hair Regrowth Company

We want to design an attractive and eye-catching sign for hair stylists and barbers to sit on their workstations to attract the attention of their clients regarding hair loss and encourage them to speak to their stylist about it of they are would like to seek treatment.
50% of men and 25% of women suffer from hair loss but most are in denial that it is happening or too embarrassed to talk about it.

Copy for the flyer is as follows:

[Section 1:]
This flyer has been placed here/designed to spark conversation about hair loss

[Section 2:]
The truth is...
73% of people believe their hair is thinning
They are right

[Section 3:]
If you've got questions, your stylist or barber has answers.

Additional Background Information:

Primary target audience is men between the ages of 25-45, secondary target audience is men 46-60

Current Consumer Perception? (in the first person) “I’ve been thinking about my hair. I think it’s getting thinner and I’m scared, worried and don’t know what to do. But I don’t know if there is anything that really works. I’ve tried other things and nothing‘s worked.”

Tonality of materials? Very guy friendly, matter of fact, authoritative, its what you might hear from your best friend. Confident. Encouraging, but with a sense of urgency.

Please use our brand colors, but do not include our logo or brand name.
Colors are as follows:
Green: #4ca26f
Light Grey: #999999
Dark Grey: #262626

I have attached print templates in both PDF and Jpeg, please use those to provide final ready to print documents if you are selected.

Target Market(s)

Industry/Entity Type

Health And Wellness

Font styles to use
Sans Serif

Colors
00a990
ffffff
333333
cbcbcb

Requirements
Must have
• We want to get across the following messaging. Ideally you will submit a design using our copy and if you think you can do better, please feel free to submit another design with your own copy/messaging. If you can do it better we would love to select you :-)
• Our copy?
• This flyer has been placed here/designed to spark conversation about hair loss
• The truth is...
• 73% of people believe their hair is thinning
• They are right
• If you've got questions, your stylist or barber has answers
• Also please use our brand colors:
• Green: #4ca26f
• Light Grey: #999999
• Dark Grey: #262626
Should not have
• dont add any logos, images or ornate design. this needs to be simple, easy to ready and eye catching.
• do not use the color red in any capacity.

```html
<!DOCTYPE html>
<html lang="en">
<head>
<meta charset="utf-8">
<title>Worried about hair loss? – Workstation Sign</title>
<link href="https://fonts.googleapis.com/css2?family=Delius&display=swap" rel="stylesheet">
<style>
  :root {
    --bg-dark: #353535;
    --accent-teal: #16a88c;
    --text-light: #f2f2f2;
  }
  html, body {
    margin: 0;
    padding: 0;
    overflow: hidden;
    background: var(--bg-dark);
  }
  .sign {
    position: relative;
    width: 806px;
    height: 1200px;
    background: var(--bg-dark);
    font-family: "Delius", "Comic Neue", sans-serif;
    color: var(--text-light);
    overflow: hidden;
  }
  .divider-band {
    position: absolute;
    left: 178px;
    width: 451px;
    height: 6px;
    background: var(--accent-teal);
  }
  .divider-band--top { top: 101px; }
  .divider-band--bottom { top: 1085px; }
  .line {
    position: absolute;
    left: 0;
    width: 100%;
    margin: 0;
    text-align: center;
    font-weight: 400;
    white-space: nowrap;
  }
  .headline {
    top: 177px;
    font-size: 61px;
    line-height: 72px;
    color: var(--accent-teal);
  }
  .subhead {
    top: 275px;
    font-size: 52px;
    line-height: 62px;
  }
  .rule-thin {
    position: absolute;
    top: 357px;
    left: 126px;
    width: 538px;
    height: 3px;
    background: var(--accent-teal);
  }
  .stat, .note, .call-to-action {
    font-size: 49px;
    line-height: 60px;
  }
  .stat-1 { top: 407px; }
  .stat-2 { top: 465px; }
  .stat-figure { color: var(--accent-teal); }
  .note-1 { top: 606px; }
  .note-2 { top: 660px; }
  .cta-1 { top: 795px; }
  .cta-2 { top: 850px; }
  .cta-3 { top: 904px; }
</style>
</head>
<body>
  <main class="sign">
    <div class="divider-band divider-band--top" role="img" aria-label="Tapered teal divider ornament"></div>

    <h1 class="line headline">Worried about hair loss?</h1>
    <p class="line subhead">Does your hair seem thinner?</p>
    <div class="rule-thin" aria-hidden="true"></div>

    <p class="line stat stat-1">Did you know that <span class="stat-figure">73%</span></p>
    <p class="line stat stat-2">of people have these fears.</p>

    <p class="line note note-1">Hair loss can occur at any age,</p>
    <p class="line note note-2">it can be difficult to talk about.</p>

    <p class="line call-to-action cta-1">If you have any concerns</p>
    <p class="line call-to-action cta-2">about your hair, speak to your</p>
    <p class="line call-to-action cta-3">barber or stylist today.</p>

    <div class="divider-band divider-band--bottom" role="img" aria-label="Tapered teal divider ornament"></div>
  </main>
</body>
</html>
```